BUILDERS MERCHANTS BUSINESS CARD

we need a business card for our long established builders merchants
we supply to both trade and diy
we offer an express delivery service
we would like TRV to standout as this our main trade mark logo
also our main colours are blue/white/yellow

Industry/Entity Type

Trade

Contact Information for Business Card

TRV BUILDERS MERCHANTS

SUPPLIERS OF ALL TYPES OF BUILDING MATERIALS

-SAND/CEMENT
-BRICKS/BLOCKS
-PLASTER/PLASTERBOARDS
-INSULATION
-FENCING/GARDEN PAVING
-PLUMBING
-ELECTRICAL
-EXPRESS DELIVERIES

EST OVER 30 YEARS

418 MARLOWE RISE
LONDON
NORWOOD
SE19 4XD

0208 5294861
0208 5392617
FAX 0208539 7283
EMAIL- TRVBUILDERSMERCHANTS@POSTVALE.CO.UK

```html
<!DOCTYPE html>
<html lang="en">
<head>
<meta charset="utf-8">
<title>TRV Builders Merchants – Business Card</title>
<link rel="stylesheet" href="https://fonts.googleapis.com/css2?family=Bebas+Neue&display=swap">
<style>
  :root {
    --stage: #5a5a5a;
    --card-white: #ffffff;
    --ink: #2b2b2b;
    --brand-blue: #448ac9;
    --brand-yellow: #f6e21b;
    --on-blue: #ffffff;
  }
  html, body {
    margin: 0;
    width: 1200px;
    height: 1000px;
    overflow: hidden;
    background: var(--stage);
    font-family: "Bebas Neue", "Arial Narrow", sans-serif;
  }
  .card {
    position: absolute;
    left: 150px;
    top: 240px;
    width: 900px;
    height: 520px;
    background: var(--card-white);
    overflow: hidden;
    color: var(--ink);
  }
  .contact-band {
    position: absolute;
    left: 0; right: 0;
    top: 292px; bottom: 0;
    background: var(--brand-blue);
  }
  .rules {
    position: absolute;
    left: 0; top: 0;
    width: 900px; height: 520px;
  }
  .brand {
    position: absolute;
    left: 310px;
    top: 32px;
    display: flex;
    align-items: center;
    gap: 8px;
  }
  .brand-mark {
    font-size: 118px;
    line-height: 0.85;
    letter-spacing: 1px;
  }
  .brand-words {
    font-size: 50px;
    line-height: 0.82;
  }
  .tagline {
    position: absolute;
    left: 0; right: 0;
    top: 146px;
    margin: 0;
    text-align: center;
    font-size: 30px;
    line-height: 30px;
    letter-spacing: 0.3px;
  }
  .products {
    position: absolute;
    top: 191px;
    margin: 0;
    padding: 0;
    list-style: none;
    font-size: 23px;
    line-height: 22px;
  }
  .products-core { left: 250px; width: 275px; text-align: right; }
  .products-services { left: 555px; width: 200px; text-align: left; }
  .contact {
    position: absolute;
    left: 0;
    top: 310px;
    display: grid;
    grid-template-columns: 335px auto;
    column-gap: 12px;
    row-gap: 0;
    margin: 0;
    color: var(--on-blue);
    font-size: 31px;
    line-height: 35px;
  }
  .contact dt { text-align: right; margin: 0; }
  .contact dd { margin: 0; }
</style>
</head>
<body>
  <section class="card" aria-label="TRV Builders Merchants business card">
    <div class="contact-band"></div>

    <svg class="rules" viewBox="0 0 900 520" aria-hidden="true">
      <g stroke="var(--brand-yellow)" stroke-width="5" fill="none">
        <line x1="0" y1="182" x2="900" y2="182"/>
        <line x1="0" y1="286" x2="900" y2="286"/>
        <line x1="250" y1="182" x2="250" y2="286"/>
        <line x1="533" y1="182" x2="533" y2="286"/>
        <line x1="545" y1="182" x2="545" y2="286"/>
        <line x1="757" y1="182" x2="757" y2="286"/>
      </g>
    </svg>

    <header class="brand">
      <span class="brand-mark">TRV</span>
      <span class="brand-words">Builders<br>Merchants</span>
    </header>

    <p class="tagline">Suppliers of all types of building materials</p>

    <ul class="products products-core">
      <li>Sand/Cement</li>
      <li>Bricks/Blocks</li>
      <li>Plaster/Plasterboards</li>
      <li>Insulation</li>
    </ul>
    <ul class="products products-services">
      <li>Fencing/Garden Paving</li>
      <li>Plumbing</li>
      <li>Electrical</li>
      <li>Express Deliveries</li>
    </ul>

    <dl class="contact">
      <dt>Address:</dt><dd>418 Marlowe Rise, London, Norwood, SE19, 4XD</dd>
      <dt>Phone:</dt><dd>0208 5294861</dd>
      <dt></dt><dd>0208 5392617</dd>
      <dt>Fax:</dt><dd>0208 5397283</dd>
      <dt>Email:</dt><dd>TRVBUILDERSMERCHANTS@POSTVALE.CO.UK</dd>
    </dl>
  </section>
</body>
</html>
```